Boutique Health and Fitness Personal Training Studio

I would like to have a brochure designed which provides a detailed description of the services offered in my business.
I have personal training studio, We look after people from early 20's to 90's, healthy to very unhealthy.
We conduct:
A consultation
An assessment
A personalised program
Personalised training sessions
I would like to base the design around the colours of my logo (attached) and use some of (or all of) the images and information I have also attached.
I would be happy with your own images included also.

Target Market(s)

20 to 90 year olds

Industry/Entity Type

Business

Font styles to use
Serif
Sans Serif

Colors
9bcb3c
add136
cadf82
eaf2ce

Requirements
Must have
• Colour and images of fitness.
• 8.5x14 legal
• Tri fold
• 2 folds with 3 faces back n front
Nice to have
• The feeling of wellbeing
Should not have
• This is not a gym.
• It should have the feel of a private relaxed environment

```html
<!DOCTYPE html>
<html lang="en">
<head>
<meta charset="utf-8">
<title>Evergreen Wellness Studio – Tri-fold Brochure</title>
<link href="https://fonts.googleapis.com/css2?family=Lato:wght@400;700;900&family=Oswald:wght@500;600&display=swap" rel="stylesheet">
<style>
:root{
  --green-deep:#4f7d1a;
  --green:#6a9a2a;
  --green-bright:#9bcb3c;
  --green-lime:#add136;
  --green-soft:#cadf82;
  --green-pale:#eaf2ce;
  --ink:#2d2d2d;
  --grey-text:#555;
  --paper:#f4f4f2;
  --backdrop:#e9e6e1;
  --bar:#2b2b2b;
}
*{box-sizing:border-box;margin:0;padding:0}
html,body{width:907px;height:1200px;overflow:hidden}
body{background:var(--backdrop);font-family:"Lato",Arial,sans-serif;position:relative}
.sheet{position:absolute;left:68px;width:792px;height:480px;box-shadow:0 6px 18px rgba(0,0,0,.35);overflow:hidden;background:#fff}
.sheet--inside{top:93px}
.sheet--outside{top:627px}
.panel{position:absolute;top:0;height:480px;overflow:hidden}
.panel--left{left:0;width:262px}
.panel--middle{left:262px;width:267px}
.panel--right{left:529px;width:263px}
.panel--paper{background:linear-gradient(90deg,#fff 0%,#e6e6e6 100%)}
.panel--green{background:linear-gradient(90deg,var(--green) 0%,var(--green-deep) 100%)}
.panel--white{background:#fff}
.abs{position:absolute}
.photo{position:absolute;overflow:hidden}
.photo--round{border-radius:50%}
h2.section{font-weight:700;font-size:12.5px;color:#1e1e1e;margin-bottom:4px}
.panel--green h2.section{color:#111}
p.copy{font-size:8.6px;line-height:1.3;color:#fff;text-align:justify}
.panel--paper p.copy{color:var(--grey-text)}
.block{position:absolute;left:28px;right:26px}
.lead{font-weight:900;font-size:13px;line-height:1.3;color:var(--green-deep)}
.brand{font-family:"Lato",Arial,sans-serif;font-weight:700;color:var(--green);display:flex;align-items:center;gap:7px;line-height:1.05}
.brand .dot{width:14px;height:14px;border-radius:50%;background:var(--green);flex:none}
.bar{position:absolute;left:0;bottom:0;width:262px;height:19px;background:var(--bar)}
.contact{position:absolute;left:0;right:0;text-align:center;color:#111;font-weight:700}
.pill{display:inline-block;background:#3a3a3a;color:var(--green-soft);font-weight:700;font-size:12.5px;padding:3px 7px;border-radius:3px;box-shadow:0 2px 3px rgba(0,0,0,.4)}
.headline{position:absolute;right:20px;text-align:right;font-family:"Oswald",Arial,sans-serif;font-weight:600;white-space:nowrap;line-height:1}
svg{display:block}
</style>
</head>
<body>

<section class="sheet sheet--inside">
  <div class="panel panel--left panel--paper">
    <div class="photo photo--round" role="img" aria-label="Woman training on a cross-trainer in the studio"
      style="left:-45px;top:-70px;width:295px;height:295px;border:5px solid #fff;box-shadow:0 0 0 5px var(--green);background:linear-gradient(135deg,#cfd4d8 0%,#8a929a 55%,#5b6168 100%)"></div>
    <svg class="abs" style="left:180px;top:215px" width="70" height="45" viewBox="0 0 70 45" aria-hidden="true">
      <path d="M5 40 C10 10 45 2 66 6 C58 30 35 44 5 40Z" fill="var(--green)"/>
    </svg>
    <div class="block" style="top:272px">
      <p class="lead">Experienced professionals caring<br>for your wellbeing</p>
    </div>
    <div class="block" style="top:314px">
      <p class="copy">Evergreen Wellness Studio have had over 25 years of experience managing the health and fitness needs of the community. Exercise programs can be designed for all levels of health and fitness and all age groups. The Studio is managed by an <b style="color:#111">Exercise Physiologist</b> with expertise in caring for people with a wide range of challenging health conditions.</p>
    </div>
    <div class="brand abs" style="left:36px;top:424px;font-size:14px"><span class="dot"></span>Evergreen<br>Wellness Studio</div>
    <div class="bar"></div>
  </div>

  <div class="panel panel--middle panel--green">
    <div class="block" style="top:32px">
      <h2 class="section">What to Expect</h2>
      <p class="copy">On arrival at the studio you will be asked to complete a questionnaire, which will provide us with information regarding your background with health and fitness, as well as your goals and objectives. Please bring any relevant medical information from medical practitioners or health professionals that you feel may impact on your program.</p>
    </div>
    <div class="block" style="top:142px">
      <h2 class="section">Consultation</h2>
      <p class="copy">A consultation will allow you to share your thoughts, concerns and objectives, as well as provide you with ample opportunity to expand on the answers from your questionnaire relating to your prior and current health, medical and physical concerns.</p>
    </div>
    <div class="block" style="top:228px">
      <h2 class="section">Assessment</h2>
      <p class="copy">An assessment will be conducted to provide us both with a baseline measure of your cardiovascular fitness, strength, flexibility, balance and body composition measures. These measures provide us with a reference for program design and also to indicate improvements along the way.</p>
    </div>
    <div class="photo" role="img" aria-label="Smiling woman seated cross-legged holding a dumbbell and a plate of vegetables"
      style="left:45px;top:312px;width:175px;height:160px;border-radius:40% 40% 20% 20%;background:radial-gradient(ellipse at 50% 45%,#f2c3cf 0%,#d9a98f 35%,rgba(80,80,80,.55) 75%,rgba(106,154,42,0) 100%)"></div>
  </div>

  <div class="panel panel--right panel--green">
    <div class="block" style="top:30px">
      <h2 class="section">The program</h2>
      <p class="copy">Your program will be designed with consideration to your health and fitness background, you objectives and your strengths and weaknesses. It will be personally tailored to your needs and provide you with a plan to focus your energies on.</p>
    </div>
    <div class="block" style="top:135px">
      <h2 class="section">Nutrition</h2>
      <p class="copy">Nutrition is central to an effective program, as it will provide you with maximal energy for exercise as well as keeping yourself lean and healthy for a long term fitter lifestyle. Evergreen Wellness Studio provides initial monitoring and ongoing modification in accordance with your needs.</p>
    </div>
    <svg class="abs" style="left:0;top:0" width="263" height="480" viewBox="0 0 263 480" aria-hidden="true">
      <path d="M12 480 C30 330 140 268 263 258 L263 480Z" fill="var(--green-bright)"/>
      <path d="M26 480 C44 342 150 282 263 272 L263 480Z" fill="#fff"/>
    </svg>
    <div class="photo" role="img" aria-label="Silhouette of a trainer guiding a woman through a lunge"
      style="left:60px;top:280px;width:200px;height:195px;background:radial-gradient(ellipse at 55% 55%,#2a2a2a 0%,#3c4a5a 40%,rgba(255,255,255,0) 72%)"></div>
  </div>
</section>

<section class="sheet sheet--outside">
  <div class="panel panel--left panel--green">
    <div class="block" style="top:36px">
      <h2 class="section">Your sessions</h2>
      <p class="copy">Training at the studio is professional and caring, but focused and challenging. Typically each session will take approximately 60 minutes. Training times can be organized to suit your needs with early mornings and evenings available.</p>
    </div>
    <div class="block" style="top:128px">
      <h2 class="section">The Cost</h2>
      <p style="color:#fff;font-size:11.5px;margin-top:6px">$45 paid in blocks of 5 or 10 sessions</p>
      <h2 class="section" style="margin-top:8px">Health fund claimable</h2>
      <p style="color:#fff;font-size:12px">Open 7 days</p>
    </div>
    <div class="abs" style="left:28px;top:226px"><span class="pill">Ample private parking available</span></div>
    <svg class="abs" style="left:0;top:0" width="262" height="480" viewBox="0 0 262 480" aria-hidden="true">
      <path d="M0 260 C120 252 228 330 256 480 L0 480Z" fill="#fff"/>
      <path d="M0 268 C116 262 218 336 244 480 L0 480Z" fill="var(--green-deep)"/>
      <path d="M218 320 C222 300 236 292 250 290 C248 310 236 320 218 320Z" fill="#fff"/>
    </svg>
    <div class="photo" role="img" aria-label="Physiotherapist treating the lower back of a man in a red shirt"
      style="left:0;top:280px;width:236px;height:200px;clip-path:path('M0 -4 C108 -10 200 56 232 200 L0 200Z');background:linear-gradient(135deg,#c9302c 0%,#a32522 40%,#e8e4e0 75%,#bfbfbf 100%)"></div>
  </div>

  <div class="panel panel--middle panel--paper">
    <div class="brand abs" style="left:48px;top:86px;font-size:17px"><span class="dot" style="width:18px;height:18px"></span>Evergreen<br>Wellness Studio</div>
    <div class="contact" style="top:134px;font-size:12.5px;line-height:1.35">Unit 12<br>Level 2</div>
    <div class="contact" style="top:170px;font-size:9.5px">48 Fernhill Road Kelmore</div>
    <div class="contact" style="top:184px;font-size:11px">call-<span style="font-size:9.5px">0400 555 172</span></div>
    <div class="contact" style="top:201px;font-size:12px">visit us</div>
    <div class="contact" style="top:217px;font-size:8.5px">www.evergreenwellness.example</div>
    <div class="photo" role="img" aria-label="Faded figure of a woman jogging"
      style="left:80px;top:240px;width:110px;height:110px;background:radial-gradient(ellipse,rgba(150,150,150,.35),rgba(230,230,230,0) 70%)"></div>
    <div class="photo" role="img" aria-label="Fresh vegetables, dumbbell, tape measure and water bottle on a table"
      style="left:0;top:345px;width:267px;height:135px;background:linear-gradient(180deg,rgba(230,230,230,0) 0%,#7fa24a 30%,#c9462e 55%,#e5c320 70%,#8a6a48 100%)"></div>
  </div>

  <div class="panel panel--right panel--white">
    <svg class="abs" style="left:0;top:0" width="263" height="480" viewBox="0 0 263 480" aria-hidden="true">
      <path d="M0 0 L263 0 L263 250 C180 262 60 272 0 230Z" fill="var(--green)"/>
      <path d="M6 482 C4 360 92 282 266 272" fill="none" stroke="var(--green)" stroke-width="13"/>
      <path d="M14 262 C18 244 34 234 54 236 C48 256 34 266 14 262Z" fill="var(--green)"/>
    </svg>
    <div class="photo" role="img" aria-label="Muscular man working out on a cable machine"
      style="left:8px;top:-20px;width:275px;height:262px;border-radius:0 0 48% 48%/0 0 40% 40%;background:linear-gradient(135deg,#3b3f44 0%,#b07a5a 45%,#6e4a36 70%,#222 100%)"></div>
    <div class="headline" style="top:348px;font-size:22px;color:var(--green)">PERSONALISED CARE</div>
    <div class="headline" style="top:378px;font-size:15.5px;color:#2a2a2a;font-weight:500">IN FITNESS AND HEALTH</div>
    <div class="brand abs" style="left:52px;top:410px;font-size:16px"><span class="dot" style="width:17px;height:17px"></span>Evergreen<br>Wellness Studio</div>
  </div>
</section>

</body>
</html>
```